Business Card: RW Office Partners - Your tidy answer finder

Business Name: RW Office Partners
Website: www.rwofficepartners.com.au
Email: marisol@rwofficepartners.com.au
Mobile: 61 487 902 346
Facebook: @rwofficepartners
Instrgram: @rwofficepartners

Brading Colours:
HEX
#986474
#ddccd3
#7a8498
#c9d8e4
#000000
#ffffff

Tag Line: Your organised problem solver

Link to DRAFT website:
https://helpdeskhub.sitebuilderx.com/rw-office-partners

About Page from the website:
My name is Marisol Bramwell, and I would love to assist you to become more productive in your day to day and achieve your business and personal goals.
My mission is to give you time, time to work on the important tasks of your business or to be able to spend more time with your family. I will take on the tasks you don’t have time for, don’t know well or simply don’t like to do.
I have an extensive background in Administration, Tender Coordination, Document Control, WHS and Quality Management working primarily in the Construction, Mining and Corporate World.
I am passionate about being organised, having order and making things in your life (and mine) easier! I love to watch something unfold and grow into something amazing! I am known for being the go-to problem solver, the organiser of all things, producing high standards of work even under pressure. I’m also a confident communicator, and I understand that you’re busy running your business.

Target Market(s)

Small to Medium Business who require assistance in their business by a virtual assistant.

Industry/Entity Type

Virtual Assistant

Contact Information for Business Card

Mobile: 61 487 902 346

Font styles to use
Sans Serif

Colors
ffffff

Requirements
Must have
• Branding Colours as outlined.
Contact Details as outlined.
Logo as provided.
Proper contact details - mobile, facebook, instragm, website.
Simple, Elegant, very clean looking.
Should not have
• Note cute with pictures.
Not too girly as still want to market to construction companies.

```html
<!DOCTYPE html>
<html lang="en">
<head>
<meta charset="utf-8">
<title>RW Office Partners – Business Card</title>
<link rel="stylesheet" href="https://fonts.googleapis.com/css2?family=Montserrat:wght@500;600&family=Oswald:wght@500&family=Roboto:wght@300;400&display=swap">
<style>
  :root {
    --backdrop: #e4e4e2;
    --card: #2d2d2e;
    --mauve: #986474;
    --mauve-soft: #ddccd3;
    --white: #ffffff;
    --rule: #8a8a8a;
    --text-sans: "Montserrat", sans-serif;
  }
  * { box-sizing: border-box; margin: 0; padding: 0; }
  html, body { width: 1200px; height: 801px; overflow: hidden; }
  body { background: var(--backdrop); position: relative; font-family: "Roboto", sans-serif; }

  .card {
    position: absolute;
    width: 560px; height: 320px;
    background: var(--card);
    border-bottom: 3px solid var(--mauve);
    box-shadow: 0 10px 24px rgba(0,0,0,.22);
    overflow: hidden;
  }
  .card--front { left: 50px; top: 70px; }
  .card--back { left: 590px; top: 410px; }

  /* front */
  .brand-name {
    position: absolute; left: 44px; top: 92px;
    font-family: var(--text-sans); font-weight: 600;
    font-size: 25px; line-height: 1.08; letter-spacing: .5px;
    text-transform: uppercase; color: var(--mauve);
  }
  .holder { position: absolute; left: 44px; top: 206px; }
  .holder__name {
    font-family: "Oswald", sans-serif; font-weight: 500;
    font-size: 30px; letter-spacing: .5px; color: var(--mauve);
    text-transform: uppercase; line-height: 1;
  }
  .holder__role {
    font-family: "Roboto", sans-serif; font-weight: 300;
    font-size: 14px; color: var(--white); margin-top: 4px; padding-left: 140px;
  }
  .divider {
    position: absolute; left: 300px; top: 150px;
    width: 1px; height: 110px; background: var(--rule);
  }
  .contacts {
    position: absolute; left: 316px; top: 150px;
    list-style: none; color: var(--white);
    font-weight: 300; font-size: 12.5px;
  }
  .contacts li { display: flex; align-items: center; gap: 9px; height: 22px; }
  .contacts svg { width: 12px; height: 12px; flex: none; }
  .contacts .accent { color: var(--mauve); }

  /* back */
  .back-title {
    position: absolute; left: 250px; top: 120px;
    font-family: var(--text-sans); font-weight: 600;
    font-size: 32px; line-height: 1.02; letter-spacing: .5px;
    text-transform: uppercase; color: var(--white);
  }
  .tagline {
    position: absolute; left: 252px; top: 202px;
    font-family: "Roboto", sans-serif; font-weight: 300;
    font-size: 15px; color: var(--white);
  }
</style>
</head>
<body>

<section class="card card--front" aria-label="Card front">
  <div class="brand-name">RW Office<br>Partners</div>

  <div class="holder">
    <div class="holder__name">Daniel Hartley</div>
    <div class="holder__role">Manager</div>
  </div>

  <div class="divider"></div>

  <ul class="contacts">
    <li>
      <svg viewBox="0 0 12 12" fill="none" stroke="#986474" stroke-width="1.2"><rect x="3" y="1" width="6" height="10" rx="1"/><line x1="5" y1="9.3" x2="7" y2="9.3"/></svg>
      61 487 902 346
    </li>
    <li>
      <svg viewBox="0 0 12 12" fill="none" stroke="#986474" stroke-width="1.2"><circle cx="6" cy="6" r="4.8"/></svg>
      @rwofficepartners
    </li>
    <li>
      <svg viewBox="0 0 12 12" fill="none" stroke="#986474" stroke-width="1.2"><rect x="1.2" y="1.2" width="9.6" height="9.6" rx="2"/></svg>
      @rwofficepartners
    </li>
    <li>
      <svg viewBox="0 0 12 12" fill="none" stroke="#986474" stroke-width="1.2"><rect x="1" y="2.5" width="10" height="7"/><polyline points="1,2.5 6,6.5 11,2.5"/></svg>
      marisol@rwofficepartners.com.au
    </li>
    <li>
      <svg viewBox="0 0 12 12" fill="none" stroke="#986474" stroke-width="1"><circle cx="6" cy="6" r="4.8"/><ellipse cx="6" cy="6" rx="2" ry="4.8"/><line x1="1.2" y1="6" x2="10.8" y2="6"/></svg>
      <span>www.<span class="accent">rwofficepartners</span>.com.au</span>
    </li>
  </ul>
</section>

<section class="card card--back" aria-label="Card back">
  <div class="back-title">RW Office<br>Partners</div>
  <div class="tagline">Your tidy answer finder</div>
</section>

</body>
</html>
```